Kitchen and cabinet shop needs new website

Benvoe Cabinets is a mid-sized, family run cabinet shop that is in the process of updating it's image after being handed over to the second generation. It's been in the business for almost 30 years and our designers have lots of experience in the design, home building and renovation industry. Our business offers free home consultations or a customer can visit our showroom to start the design process. Whether the client is a designer, home builder or homeowner we can help create the kitchen and space you're after by helping every step of the way.

The website needs to showcase our past work, (pictures to be included), show the different styles (eg. traditional, modern) and different areas of the home we can produce cabinets for. We created a new logo with Sketch hive that needs to be included in the website as well as the colours. I would like 5 pages;
-Home page
-About us
-portfolio/gallery
-services
-contact us

I would like the website to have a contemporary look, nothing too busy or complicated.

I will attach some pictures with the different styles of our work I mentioned above and provide content for each job.
Updates

Target Market(s)

home owners, designer, home builders, business owners

Industry/Entity Type

Home Builder

Number of Pages Required

5+ page

Font styles to use
Sans Serif

Requirements
Must have
• home page, about us page, gallery/portfolio page-showing various pictures of our work and different styles, services page and contact us.
• Use logo and similar colours as in logo for the scheme
• more content and pictures to follow...

```html
<!DOCTYPE html>
<html lang="en">
<head>
<meta charset="utf-8">
<title>Benvoe Cabinets — Home</title>
<link href="https://fonts.googleapis.com/css2?family=Raleway:wght@300;400;500&family=Open+Sans:wght@400;700&display=swap" rel="stylesheet">
<style>
:root{
  --blue:#1f62b0;
  --orange:#f47421;
  --ink:#111;
  --muted:#8a8a8a;
  --text:#555;
  --topbar:#f6f6f6;
  --rule:#e2e2e2;
}
*{margin:0;padding:0;box-sizing:border-box}
html,body{width:953px;height:1200px;overflow:hidden;background:#fff}
body{position:relative;font-family:"Open Sans",sans-serif;color:var(--text)}
.topbar{position:absolute;top:0;left:0;width:953px;height:30px;background:var(--topbar);border-bottom:1px solid var(--rule)}
.topbar .phone{position:absolute;right:83px;top:7px;display:flex;align-items:center;gap:6px;color:var(--blue);font-weight:700;font-size:12px}
.header{position:absolute;top:30px;left:0;width:953px;height:102px}
.brand{position:absolute;left:75px;top:18px;display:flex;align-items:center;gap:10px}
.brand-mark{width:40px;height:56px;background:var(--blue)}
.brand-name{font-family:"Raleway",sans-serif;font-weight:500;font-size:27px;color:var(--blue);letter-spacing:1px;line-height:1;text-transform:uppercase}
.brand-tag{font-size:9px;letter-spacing:1.6px;color:#333;margin-top:6px}
.nav{position:absolute;top:35px;right:80px;display:flex;gap:39px;font-family:"Raleway",sans-serif;font-size:17px;color:var(--muted)}
.nav .active{color:var(--orange)}
.hero{position:absolute;top:132px;left:0;width:953px;height:636px;
  background:linear-gradient(180deg,#c9c9c7 0%,#e4e4e2 30%,#d7d8d8 55%,#8e8f91 72%,#3c3431 100%)}
.dots{position:absolute;bottom:19px;left:418px;display:flex;gap:17px}
.dots span{width:16px;height:16px;background:#fff}
.dots .on{background:var(--orange)}
.welcome{position:absolute;top:812px;left:0;width:953px;text-align:center;font-family:"Raleway",sans-serif;font-weight:300;font-size:35px;color:var(--ink)}
.welcome .b{color:var(--blue)}.welcome .o{color:var(--orange)}
.intro{position:absolute;top:888px;left:76px;width:801px;text-align:center;font-size:12px;line-height:18.2px;white-space:nowrap}
.footer{position:absolute;top:1022px;left:0;width:953px;height:178px;background:var(--blue);color:#fff}
.fnav{position:absolute;left:61px;top:23px;display:flex;align-items:center;gap:20px;font-family:"Raleway",sans-serif;font-size:15px}
.fnav a{padding:8px 19px;color:#fff;text-decoration:none}
.fnav .active{border:1px solid #fff;border-radius:20px}
.fnav a:not(.active){padding:8px 0;margin-right:19px}
.social{position:absolute;right:81px;top:42px;width:17px;height:17px;background:#fff}
.rule{position:absolute;left:61px;top:84px;width:831px;height:1px;background:rgba(255,255,255,.35)}
.fhead{position:absolute;left:106px;top:96px;font-size:19px}
.item{position:absolute;top:120px;display:flex;align-items:center;gap:9px;font-size:11px;line-height:18px}
.ico{width:33px;height:33px;border-radius:50%;background:#fff;display:flex;align-items:center;justify-content:center;flex:none}
.item.addr .ico{background:#2d7de0}
.copy{position:absolute;right:65px;top:129px;font-size:11px}
</style>
</head>
<body>
<div class="topbar"><div class="phone">
  <svg width="10" height="15" viewBox="0 0 10 15"><rect x="1" y="1" width="8" height="13" rx="1.5" fill="none" stroke="#f47421" stroke-width="2"/><rect x="4" y="11" width="2" height="1.5" fill="#f47421"/></svg>
  604.555.0182</div></div>

<header class="header">
  <div class="brand">
    <div class="brand-mark"></div>
    <div><div class="brand-name">Benvoe Cabinets</div><div class="brand-tag">Custom woodwork and cabinetry</div></div>
  </div>
  <nav class="nav"><span class="active">Home</span><span>About</span><span>Gallery</span><span>Services</span><span>Contact</span></nav>
</header>

<section class="hero" role="img" aria-label="Bright modern kitchen with white cabinets, grey island and chrome bar stools">
  <div class="dots"><span></span><span></span><span class="on"></span><span></span></div>
</section>

<h1 class="welcome">WELCOME TO <span class="b">BENVOE</span> <span class="o">CABINETS</span></h1>
<p class="intro">Benvoe Cabinets understands how important your home is to you and your family. That’s why<br>we’re dedicated to ensure you get exactly what you deserve. For nearly 30 years we’ve been improving every<br>area of your home with our designs and skilled wood workers. Our attention to detail and high standard of quality is<br>what makes Benvoe Cabinets truly unique. Please visit us at our design center or schedule an in home consultation and we can<br>help to build your dream and make it a reality.</p>

<footer class="footer">
  <nav class="fnav"><a class="active">Home</a><a>About</a><a>Gallery</a><a>Services</a><a>Contact</a></nav>
  <div class="social" aria-label="Social profile"></div>
  <div class="rule"></div>
  <div class="fhead">Contact Us</div>
  <div class="item addr" style="left:61px">
    <span class="ico"><svg width="16" height="14" viewBox="0 0 16 14"><path d="M8 1 1 7h2v6h4V9h2v4h4V7h2z" fill="#fff"/></svg></span>
    <span>2276 Alderglen Crescent,<br>Burnaby, B.C. V5B 4K8</span>
  </div>
  <div class="item" style="left:273px">
    <span class="ico"><svg width="10" height="15" viewBox="0 0 10 15"><rect x="1" y="1" width="8" height="13" rx="1.5" fill="none" stroke="#f47421" stroke-width="2"/></svg></span>
    <span>Call : 604.555.0182</span>
  </div>
  <div class="item" style="left:419px">
    <span class="ico"><svg width="16" height="14" viewBox="0 0 16 14"><rect x="4" y="0" width="8" height="4" fill="#f47421"/><rect x="0" y="5" width="16" height="6" rx="1" fill="#f47421"/><rect x="4" y="9" width="8" height="5" fill="#fff" stroke="#f47421"/></svg></span>
    <span>Fax : 604.555.0147</span>
  </div>
  <div class="copy">© <b>BENVOE CABINET</b> - 2015. All Rights Reserved.</div>
</footer>
</body>
</html>
```